BCR 2014 Seasons Greetings

Christmas postcards.
Side A: Image with 3 logos "Vareno Cove Lodge" "Kilimu Lodge Samoa" "Sefa Lani"(Logos on bottom of card" & "Seasons Greetings" (to fit)
Side B Left:
Text
"Management and staff at Orrinvale Lodges wish you and your family a very happy and safe festive season and all the best for the New Year.
Counting down your next arrival"
Side B Right: Address template with 4 lines & Area for stamp top right corner.
Side B Base: Logo & Website "Orrinvale Lodges" " www.orrinvalelodges.example"
High end travel
Management

```html
<!DOCTYPE html>
<html lang="en">
<head>
<meta charset="utf-8">
<title>Orrinvale Lodges – Seasons Greetings Postcard</title>
<link rel="stylesheet" href="https://fonts.googleapis.com/css2?family=Yellowtail&family=Great+Vibes&family=Josefin+Sans:wght@600&display=swap">
<style>
  :root {
    --backdrop: #1e1e1e;
    --card-white: #ffffff;
    --brand-blue: #2a76b9;
    --ink-dark: #222222;
    --rule-grey: #555555;
    --stamp-grey: #c4c4c4;
    --tone-sea: #8ec3da;
    --tone-night: #1f2a1f;
    --tone-dusk: #343a8c;
    --tone-sand: #c9c3b8;
  }
  * { box-sizing: border-box; margin: 0; padding: 0; }
  html, body {
    width: 859px; height: 1200px; overflow: hidden;
    background: var(--backdrop);
  }
  .canvas { position: relative; width: 859px; height: 1200px; }

  /* ---------- Side A ---------- */
  .card-front {
    position: absolute; left: 84px; top: 36px; width: 703px; height: 545px;
    background: var(--card-white);
  }
  .photo { position: absolute; }
  .photo-wave      { left: 0;     top: 0;     width: 414px; height: 204px; background: var(--tone-sea); }
  .photo-fireworks { left: 418px; top: 0;     width: 285px; height: 270px; background: var(--tone-night); }
  .photo-sunset    { left: 0;     top: 209px; width: 414px; height: 230px; background: var(--tone-dusk); }
  .photo-sand      { left: 418px; top: 274px; width: 285px; height: 165px; background: var(--tone-sand); }
  .band-rule {
    position: absolute; left: 0; top: 441px; width: 703px; height: 2px;
    background: var(--brand-blue);
  }
  .greeting-title {
    position: absolute; left: 12px; top: 464px; width: 345px;
    font-family: "Yellowtail", cursive; font-weight: 400;
    font-size: 44px; line-height: 1; color: var(--brand-blue);
    white-space: nowrap; overflow: hidden;
  }
  .greeting-swoosh { position: absolute; left: 12px; top: 504px; }
  .lodge-name {
    position: absolute; top: 478px; width: 120px;
    display: flex; flex-direction: column; align-items: center; gap: 10px;
    font-family: "Josefin Sans", sans-serif; font-weight: 600;
    font-size: 8px; letter-spacing: 0.6px; text-transform: uppercase;
    color: var(--ink-dark); white-space: nowrap;
  }
  .lodge-vareno { left: 366px; }
  .lodge-sefa   { left: 478px; }
  .lodge-kilimu { left: 580px; }
  .lodge-dot {
    width: 24px; height: 24px; border-radius: 50%;
    background: var(--ink-dark);
  }

  /* ---------- Side B ---------- */
  .card-back {
    position: absolute; left: 84px; top: 637px; width: 703px; height: 545px;
    background: var(--card-white);
  }
  .message-panel {
    position: absolute; left: 0; top: 0; width: 343px; height: 545px;
    background: var(--brand-blue);
    color: var(--card-white); text-align: center;
    font-family: "Great Vibes", cursive;
  }
  .message-body {
    position: absolute; left: 0; top: 14px; width: 343px;
    font-size: 29px; line-height: 48px;
  }
  .message-newyear {
    position: absolute; left: 0; top: 260px; width: 343px;
    font-size: 40px; line-height: 1;
  }
  .message-signoff {
    position: absolute; left: 0; top: 348px; width: 343px;
    font-size: 27px; line-height: 1;
  }
  .stamp-box {
    position: absolute; left: 528px; top: 17px; width: 158px; height: 157px;
    border: 2px solid var(--stamp-grey);
  }
  .address-line {
    position: absolute; left: 374px; width: 305px; height: 1px;
    background: var(--rule-grey);
  }
</style>
</head>
<body>
<main class="canvas">

  <section class="card-front" aria-label="Postcard front">
    <div class="photo photo-wave" role="img" aria-label="Photo: ocean wave with an island in the distance"></div>
    <div class="photo photo-fireworks" role="img" aria-label="Photo: fireworks with a palm tree at night"></div>
    <div class="photo photo-sunset" role="img" aria-label="Photo: sunset over a lagoon"></div>
    <div class="photo photo-sand" role="img" aria-label="Photo: lodge name written on sand with shells"></div>
    <div class="band-rule"></div>

    <h1 class="greeting-title">Seasons Greetings</h1>
    <svg class="greeting-swoosh" width="350" height="24" viewBox="0 0 350 24" aria-hidden="true">
      <path d="M4 20 Q 150 2 345 14" fill="none" stroke="#2a76b9" stroke-width="3" stroke-linecap="round"/>
    </svg>

    <div class="lodge-name lodge-vareno"><span class="lodge-dot"></span>Vareno Cove Lodge</div>
    <div class="lodge-name lodge-sefa"><span class="lodge-dot"></span>Sefa Lani</div>
    <div class="lodge-name lodge-kilimu"><span class="lodge-dot"></span>Kilimu Lodge Samoa</div>
  </section>

  <section class="card-back" aria-label="Postcard back">
    <div class="message-panel">
      <p class="message-body">Management and staff at<br>Orrinvale Lodges wish you<br>and your family a very<br>happy and safe festive season<br>and all the best for the</p>
      <p class="message-newyear">New Year</p>
      <p class="message-signoff">Counting down your next arrival</p>
    </div>
    <div class="stamp-box" aria-label="Stamp area"></div>
    <div class="address-line" style="top:269px"></div>
    <div class="address-line" style="top:329px"></div>
    <div class="address-line" style="top:389px"></div>
    <div class="address-line" style="top:449px"></div>
  </section>

</main>
</body>
</html>
```